Curbside Twisters Grand Opening 2-for-1 Sale Postcard Design

Who we are: Curbside Twisters will come to you. We roll your medical marijuana in the privacy and safety of your home. We roll your medicine for you.

We need a postcard design that meets NDPX EDDM requirements for our Grand Opening 2-for-1 Sale. Please include some or all of our logo.
Looking for elegant, upscale design. Appeal to luxury buyers with more money than time.
I uploaded DraftDiy image of my own draft just to show basic content needs of this project.
Updates

2-for-1 offer good thru March 31, 2015.Please add a small recycle image to convey the fact that we recycle. Added Tuesday, December 8, 2015

Target Market(s)

Income $50K+, Age 35+, College education, Left politically, No kids or older kids

Industry/Entity Type

Health Service

Requirements
Must have
• Our logo
• Our contact number: (989) 555-0172
• NDPX Postcard/EDDM comptability layout on back of card.
• 2-for-1 Offer good thru March 31st, 2016.
Nice to have
• 2-3 colors, white text on dark green background
Should not have
• Images of marijuana. Please limit marijuana images to our logo.

```html
<!DOCTYPE html>
<html lang="en">
<head>
<meta charset="utf-8">
<title>Curbside Twisters – Grand Opening Postcard</title>
<link rel="stylesheet" href="https://fonts.googleapis.com/css2?family=Alegreya+SC:wght@800&family=Open+Sans:ital,wght@0,400;0,600;0,700;1,300;1,400&family=Arimo:wght@400;700&display=swap">
<style>
  :root{
    --green:#3f7d2a;
    --green-deep:#2b611d;
    --green-shade:#22501a;
    --ribbon:#5cb548;
    --ribbon-dark:#479a36;
    --ribbon-edge:#d3e98a;
    --ribbon-text:#ffffff;
    --mark:#6cc455;
    --white:#ffffff;
    --ink:#111111;
    --paper:#ffffff;
    --strip:#eeeeee;
    --star:#e7e4c8;
  }
  *{margin:0;padding:0;box-sizing:border-box}
  html,body{width:1200px;height:848px;overflow:hidden;background:var(--paper)}
  body{position:relative;font-family:"Open Sans",sans-serif;color:var(--white)}

  .card{position:absolute;overflow:hidden;box-shadow:0 2px 10px rgba(0,0,0,.35)}
  .card-front{left:26px;top:27px;width:575px;height:728px;
    background:radial-gradient(ellipse at 50% 45%,var(--green) 0%,var(--green-deep) 75%,var(--green-shade) 100%)}
  .card-back{left:606px;top:96px;width:573px;height:731px;background:var(--paper)}
  .back-panel{position:absolute;left:0;top:0;width:573px;height:461px;
    background:radial-gradient(ellipse at 50% 40%,var(--green) 0%,var(--green-deep) 80%,var(--green-shade) 100%)}
  .back-strip{position:absolute;left:0;bottom:0;width:100%;height:37px;background:var(--strip)}

  .center{position:absolute;left:0;width:100%;text-align:center}
  .ribbon{position:absolute;left:0;width:575px}
  .ribbon-top{top:36px;height:140px}
  .ribbon-offer{top:440px;height:100px}
  .ribbon text{font-family:"Alegreya SC",serif;font-weight:800;fill:var(--ribbon-text)}
  .ribbon .ribbon-sub{font-family:"Open Sans",sans-serif;font-style:italic;font-weight:400}

  .date{top:117px;font-weight:600;font-size:26px;letter-spacing:.2px}
  .brand-mark{position:absolute;border-radius:50%;background:var(--mark)}
  .front-mark{left:239px;top:190px;width:96px;height:96px}
  .back-mark{left:251px;top:32px;width:72px;height:72px}
  .brand-name{font-family:"Open Sans",sans-serif;font-weight:600;color:var(--white);white-space:nowrap}
  .front-brand{top:316px;font-size:51px;letter-spacing:-1px;line-height:1.2}
  .tagline{position:absolute;left:82px;top:389px;font-style:italic;font-weight:300;font-size:20px}
  .book{top:558px;font-style:italic;font-weight:300;font-size:28px;line-height:1.3}
  .phone{top:598px;font-weight:700;font-size:42px;letter-spacing:-.5px;line-height:1.3}
  .site{top:657px;font-size:19px;letter-spacing:.3px;line-height:1.3}

  .stars{position:absolute;top:533px;width:88px;height:80px;border-radius:14px;
    background:linear-gradient(160deg,rgba(231,228,200,.55),rgba(231,228,200,.25))}
  .stars-left{left:36px}
  .stars-right{left:457px}

  .back-brand{top:116px;font-size:38px;letter-spacing:-1px;line-height:1.2}
  .back-copy{position:absolute;left:51px;width:471px;text-align:center;font-size:13.2px;line-height:21px}
  .section-title{top:186px;font-size:15px}
  .what{top:217px}
  .what b{font-weight:700}
  .book-line{top:266px}
  .contact{top:295px;font-size:12.8px;line-height:19.5px}
  .contact .caps{font-size:11.3px}
  .serving{top:404px;font-style:italic}

  .address-box{position:absolute;left:77px;top:527px;width:299px;height:98px;border:2.5px solid var(--ink);color:var(--ink);font-family:"Arimo",sans-serif}
  .address-box .route{position:absolute;top:12px;left:0;width:100%;text-align:center;font-size:13px}
  .address-box .recipient{position:absolute;left:20px;top:44px;font-size:17px;line-height:1.2}
  .indicia{position:absolute;left:403px;top:531px;width:92px;height:92px;border:1px solid var(--ink);color:var(--ink);font-family:"Arimo",sans-serif;font-size:11px;line-height:1.35;text-align:center;padding-top:9px;letter-spacing:-.3px}
  .indicia b{font-weight:700}
</style>
</head>
<body>

<section class="card card-front" aria-label="Postcard front">
  <svg class="ribbon ribbon-top" viewBox="0 0 575 140">
    <polygon points="14,62 120,46 120,110 14,124 46,92" fill="var(--ribbon-dark)" stroke="var(--ribbon-edge)" stroke-width="2"/>
    <polygon points="561,62 455,46 455,110 561,124 529,92" fill="var(--ribbon-dark)" stroke="var(--ribbon-edge)" stroke-width="2"/>
    <path d="M82,34 Q287,-6 493,34 L493,104 Q287,64 82,104 Z" fill="var(--ribbon)" stroke="var(--ribbon-edge)" stroke-width="2"/>
    <path id="arc-grand" d="M90,86 Q287,40 485,86" fill="none"/>
    <text font-size="46" text-anchor="middle" letter-spacing="1"><textPath href="#arc-grand" startOffset="50%">GRAND OPENING</textPath></text>
  </svg>

  <p class="center date">JANUARY 2016</p>

  <div class="brand-mark front-mark"></div>
  <p class="center brand-name front-brand">Curbside Twisters</p>
  <p class="tagline">So you don't have to.</p>

  <svg class="ribbon ribbon-offer" viewBox="0 0 575 100">
    <polygon points="118,42 180,34 180,86 118,94 140,66" fill="var(--ribbon-dark)" stroke="var(--ribbon-edge)" stroke-width="2"/>
    <polygon points="457,42 395,34 395,86 457,94 435,66" fill="var(--ribbon-dark)" stroke="var(--ribbon-edge)" stroke-width="2"/>
    <path d="M160,22 Q287,2 415,22 L415,78 Q287,58 160,78 Z" fill="var(--ribbon)" stroke="var(--ribbon-edge)" stroke-width="2"/>
    <path id="arc-offer" d="M166,50 Q287,28 409,50" fill="none"/>
    <path id="arc-offer-sub" d="M172,68 Q287,50 403,68" fill="none"/>
    <text font-size="30" text-anchor="middle"><textPath href="#arc-offer" startOffset="50%">2 FOR 1 SPECIAL</textPath></text>
    <text class="ribbon-sub" font-size="12.5" text-anchor="middle"><textPath href="#arc-offer-sub" startOffset="50%">Good through March 31, 2016</textPath></text>
  </svg>

  <div class="stars stars-left" role="img" aria-label="Cluster of cream stars"></div>
  <div class="stars stars-right" role="img" aria-label="Cluster of cream stars"></div>

  <p class="center book">Book Today!</p>
  <p class="center phone">(989) 555-0172</p>
  <p class="center site">WWW.CURBSIDETWISTERS.COM</p>
</section>

<section class="card card-back" aria-label="Postcard back">
  <div class="back-panel">
    <div class="brand-mark back-mark"></div>
    <p class="center brand-name back-brand">Curbside Twisters</p>
    <p class="back-copy section-title">WHAT WE DO</p>
    <p class="back-copy what"><b>Curbside Twisters</b> will come to you. We roll your medical marijuana in the privacy and safety of your home. <b>We roll your medicine for you.</b></p>
    <p class="back-copy book-line">Make an Appointment Today!&nbsp; To book your roller:</p>
    <p class="back-copy contact">Call us at (989) 555-0172 OR<br>Email us <span class="caps">APPOINTMENTS@CURBSIDETWISTERS.COM</span> with your preferred appointment time, date and roll quantity. Please include your address so we can estimate appointment duration.</p>
    <p class="back-copy serving">Serving Gaylord and Petoskey</p>
  </div>

  <div class="address-box">
    <p class="route">******************ECRWSS****</p>
    <p class="recipient">Local<br>Postal Customer</p>
  </div>
  <div class="indicia">PRSRT STD<br>ECRWSS<br>NDPX POSTAGE<br><b>PAID</b><br>EDDM RETAIL</div>

  <div class="back-strip"></div>
</section>

</body>
</html>
```